Transportation Brokerage and Freight Forwarder

We need a Facebook company page to attract potential customers (Shippers) and potential Drivers (Truck Drivers) for our business. We provide nationwide shipping services for contract customers in all areas of the Supply Chain LTL (Less than Truck Load), TL (Truck Load) Sea Freight (Ocean Vessels), Air Freight (Air Cargo), Container Freight, Rail Freight (Trains). We are also a Transportation Consulting Company as well helping clients to create Shipping solutions to improve there shipping capacity or cut cost by suggesting different modes of transport based upon their needs.

We have over 50+ years experience in the industry to include Driving (myself and my partner still hold CDL licenses currently), Dispatching Management, Operations Management and former Transport Executives, we are also doing work in other countries with our strategic partners in the form of Freight forwarding services that we offer.

Target Market(s)

The Transport and Shipping community in the U.S., Truck, Train, Ship, Plane & Container

Font styles to use
Serif
Sans Serif

Colors

Designer to choose colors to be used in the design.

Requirements
Must have
• Targeted services we provide (use our website for ideas) www.vrnhtp.com. We want to get the name out there, use stock photos from the Logistics industry
Nice to have
• Appealing attraction to the page itself, want to draw views
Should not have
• No overkill of information

```html
<!DOCTYPE html>
<html lang="en">
<head>
<meta charset="utf-8">
<title>Route Harbor Partners – Facebook Cover</title>
<link rel="stylesheet" href="https://fonts.googleapis.com/css2?family=Teko:wght@500&family=Noto+Serif&family=Montserrat:wght@500;600&display=swap">
<style>
  :root {
    --page-bg: #e9eef2;
    --navy: #05344a;
    --brand-blue: #0a8ac8;
    --bright-cyan: #19b3ea;
    --white: #ffffff;
  }
  html, body {
    margin: 0;
    width: 1200px;
    height: 1200px;
    overflow: hidden;
    background: var(--page-bg);
  }
  .cover {
    position: absolute;
    left: 48px;
    top: 390px;
    width: 1104px;
    height: 420px;
    overflow: hidden;
    background: var(--navy);
  }
  .cover-shapes {
    position: absolute;
    inset: 0;
    width: 100%;
    height: 100%;
  }
  .brand-column {
    position: absolute;
    left: 0;
    top: 0;
    width: 608px;
    text-align: center;
    color: var(--white);
  }
  .brand-mark {
    width: 58px;
    height: 58px;
    margin: 34px auto 0;
    border-radius: 50%;
    background: var(--brand-blue);
  }
  .brand-name,
  .brand-descriptor {
    margin: 0;
    font-family: "Noto Serif", serif;
    font-size: 20px;
    line-height: 26px;
  }
  .brand-name { margin-top: 22px; }
  .headline {
    margin: 21px 0 0;
    font-family: "Teko", sans-serif;
    font-weight: 500;
    font-size: 64px;
    line-height: 60px;
    letter-spacing: 0.3px;
    text-transform: uppercase;
  }
  .quote-button {
    display: inline-flex;
    align-items: center;
    gap: 14px;
    margin-top: 22px;
    height: 43px;
    padding: 0 10px 0 18px;
    border-radius: 8px;
    background: linear-gradient(180deg, #1d6fae 0%, #0d4f86 100%);
    box-shadow: 0 2px 6px rgba(0,0,0,0.35);
    font-family: "Montserrat", sans-serif;
    font-weight: 500;
    font-size: 18px;
    color: var(--white);
  }
  .quote-icon {
    width: 30px;
    height: 30px;
  }
  .contact-box {
    position: absolute;
    left: 904px;
    top: 300px;
    width: 172px;
    height: 104px;
    box-sizing: border-box;
    border: 1.5px solid var(--bright-cyan);
    text-align: center;
    font-family: "Montserrat", sans-serif;
    color: var(--white);
  }
  .contact-title {
    margin: 0 0 6px;
    padding: 5px 0 5px;
    border-bottom: 1.5px solid var(--bright-cyan);
    color: var(--bright-cyan);
    font-weight: 600;
    font-size: 15px;
    line-height: 18px;
  }
  .contact-line {
    margin: 0;
    font-size: 14px;
    line-height: 18px;
    font-weight: 500;
  }
  .contact-web {
    margin: 1px 0 0;
    font-size: 16px;
    line-height: 20px;
    font-weight: 500;
  }
</style>
</head>
<body>
  <section class="cover">
    <svg class="cover-shapes" viewBox="0 0 828 315" preserveAspectRatio="none" xmlns="http://www.w3.org/2000/svg">
      <defs>
        <linearGradient id="photoTone" x1="0" y1="0" x2="0" y2="1">
          <stop offset="0" stop-color="#c9cfe3"/>
          <stop offset="0.55" stop-color="#a9b4cf"/>
          <stop offset="1" stop-color="#6f7f9c"/>
        </linearGradient>
      </defs>
      <path class="swoosh-white-base" d="M390,0 L828,0 L828,315 L560,315 C550,190 490,60 390,0 Z" fill="#ffffff"/>
      <path class="swoosh-blue" d="M375,0 C470,80 540,220 336,315 L569,315 C560,190 500,60 395,0 Z" fill="#0a8ac8"/>
      <path class="swoosh-navy-gap" d="M378,315 C490,250 505,130 440,40 C520,110 535,220 526,315 Z" fill="#05344a"/>
      <path class="swoosh-white-stripe" d="M482,315 C498,240 495,170 478,105 C508,160 520,240 516,315 Z" fill="#ffffff"/>
      <g role="img" aria-label="Photo of a white semi truck and a truck driver under an evening sky">
        <path d="M414,0 L828,0 L828,188 C720,200 640,240 612,290 C590,180 530,50 414,0 Z" fill="url(#photoTone)"/>
      </g>
      <path class="contact-panel" d="M604,315 C640,240 720,200 828,188 L828,315 Z" fill="#05344a"/>
      <path class="contact-panel-edge" d="M604,315 C640,240 720,200 828,188" fill="none" stroke="#ffffff" stroke-width="4"/>
    </svg>

    <div class="brand-column">
      <div class="brand-mark"></div>
      <p class="brand-name">Route Harbor Partners</p>
      <p class="brand-descriptor">Transportation Brokers</p>
      <h1 class="headline">Route Harbor Partners<br>"We Listen, We Deliver"</h1>
      <div class="quote-button">
        <span>GET A QUOTE</span>
        <svg class="quote-icon" viewBox="0 0 30 30" aria-hidden="true">
          <rect x="2" y="4" width="22" height="20" rx="2" fill="#dfe8f1"/>
          <circle cx="20" cy="19" r="8" fill="#ffffff" stroke="#6c7f92" stroke-width="1.5"/>
          <path d="M20,14 L20,19 L23,21" fill="none" stroke="#33475b" stroke-width="1.5"/>
        </svg>
      </div>
    </div>

    <div class="contact-box">
      <p class="contact-title">CONTACT US NOW!</p>
      <p class="contact-line">888-555-0142</p>
      <p class="contact-line">706-555-0187</p>
      <p class="contact-web">www.vrnhtp.com</p>
    </div>
  </section>
</body>
</html>
```